Public Speaking Book for aspiring, ambitious speakers

I'm looking for a 6x9 book cover (Parcelo standard) as well as ebook and audiobook formats.

I'm looking for orange font on a white background as these are my brand colours.

Feel free to use some yellow and gold too if you deem it appropriate.

Title: Climb and Glow
Subtitle: Find Your Voice. Tell Your Story. Share your Message.
Author: Lionel Barstow

I would like to have a picture of a female speaker on the front cover.

Alternatively, some kind of image that symbolises public speaking like a microphone, podium etc

Target Market(s)

Aspiring professional speakers

Colors
f78f20

Requirements
Must have
• Correct spelling!
Nice to have
• A logo or picture that fits the theme, but no pressure if you can't think of anything
Should not have
• No men in suits please. I don't want this to have a 1980s corporate look.

```html
<!DOCTYPE html>
<html lang="en">
<head>
<meta charset="utf-8">
<title>Climb and Glow – Cover Spread</title>
<link rel="stylesheet" href="https://fonts.googleapis.com/css2?family=Bebas+Neue&family=Montserrat:ital,wght@0,400;1,600&family=Oswald:wght@500&display=swap">
<style>
  :root {
    --brand-orange: #f78f20;
    --paper-white: #ffffff;
    --stage-grey: #efefef;
    --ink-dark: #3a3a3a;
    --photo-light: #f6efea;
    --photo-mid: #e9ddd6;
  }
  * { margin: 0; padding: 0; box-sizing: border-box; }
  html, body { width: 899px; height: 1200px; overflow: hidden; }
  body { background: var(--stage-grey); position: relative; }

  .cover-spread {
    position: absolute;
    left: 11px; top: 296px;
    width: 877px; height: 607px;
    background: var(--brand-orange);
    overflow: hidden;
  }

  /* Back cover */
  .back-title {
    position: absolute;
    right: 503px; top: 30px;
    text-align: right;
    font-family: "Bebas Neue", sans-serif;
    color: var(--paper-white);
    line-height: 0.92;
  }
  .back-title .line-one { display: block; font-size: 72px; }
  .back-title .line-two { display: block; font-size: 62px; }
  .back-rule {
    position: absolute;
    left: 0; top: 143px;
    width: 374px; height: 4px;
    background: var(--paper-white);
  }
  .back-blurb {
    position: absolute;
    left: 32px; top: 168px;
    width: 341px;
    font-family: "Montserrat", sans-serif;
    font-size: 10.6px;
    line-height: 13.4px;
    color: var(--paper-white);
    text-align: justify;
  }
  .back-blurb p + p { margin-top: 13px; }
  .price-box {
    position: absolute;
    left: 36px; top: 518px;
    width: 89px; height: 53px;
    background: var(--paper-white);
  }

  /* Spine */
  .spine-title, .spine-author {
    position: absolute;
    transform: rotate(-90deg);
    text-align: center;
    color: var(--paper-white);
    white-space: nowrap;
  }
  .spine-title {
    left: 291px; top: 148px;
    width: 300px; height: 46px;
    font-family: "Bebas Neue", sans-serif;
    font-size: 54px;
    line-height: 46px;
  }
  .spine-author {
    left: 320px; top: 443px;
    width: 240px; height: 24px;
    font-family: "Oswald", sans-serif;
    font-weight: 500;
    font-size: 17px;
    line-height: 24px;
    letter-spacing: 0.42em;
  }

  /* Front cover */
  .front-cover {
    position: absolute;
    left: 472px; top: 0;
    width: 405px; height: 607px;
    background: var(--paper-white);
  }
  .cover-photo {
    position: absolute;
    left: 0; top: 0;
    width: 405px; height: 555px;
  }
  .front-title {
    position: absolute;
    left: 21px; top: 22px;
    font-family: "Bebas Neue", sans-serif;
    color: var(--brand-orange);
    line-height: 0.86;
  }
  .front-title .line-one { display: block; font-size: 112px; }
  .front-title .line-two { display: block; font-size: 96px; }
  .front-rule {
    position: absolute;
    left: 0;
    width: 274px; height: 4px;
    background: var(--brand-orange);
  }
  .front-rule.upper { top: 216px; }
  .front-rule.lower { top: 305px; }
  .subtitle {
    position: absolute;
    left: 21px; top: 231px;
    font-family: "Montserrat", sans-serif;
    font-style: italic;
    font-weight: 600;
    font-size: 18px;
    line-height: 21px;
    color: var(--ink-dark);
  }
  .author-band {
    position: absolute;
    left: 0; top: 555px;
    width: 405px; height: 52px;
    background: var(--brand-orange);
    font-family: "Oswald", sans-serif;
    font-weight: 500;
    font-size: 27px;
    line-height: 52px;
    letter-spacing: 0.36em;
    text-align: center;
    color: var(--paper-white);
    padding-left: 0.36em;
    white-space: nowrap;
  }
</style>
</head>
<body>
  <main class="cover-spread">
    <section class="back-cover">
      <h2 class="back-title">
        <span class="line-one">CLIMB AND</span>
        <span class="line-two">GLOW</span>
      </h2>
      <div class="back-rule"></div>
      <div class="back-blurb">
        <p>Lorem ipsum dolor sit amet, consectetur adipiscing elit. Aliquam pulvinar convallis turpis, a ultrices augue tempus id. Nullam et mi ante. Vestibulum ac luctus arcu. Vestibulum ac aliquet felis. In auctor efficitur nisi, lacinia commodo lectus maximus at. Vestibulum tincidunt commodo magna tempus ullamcorper. Praesent fringilla hendrerit erat eu elementum. Donec facilisis nisi purus. Nulla vitae velit sem. Cras sit amet vestibulum augue. Aliquam mattis massa ut quam consectetur scelerisque. In tempor gravida sem, vel blandit orci molestie feugiat. Quisque ut hendrerit quam, ac cursus massa. Donec ac ipsum leo.</p>
        <p>Morbi laoreet efficitur ullamcorper. Maecenas eu euismod urna. Nam efficitur, diam at bibendum viverra, lacus ipsum finibus diam, in auctor dolor dui vitae nulla. Phasellus eu bibendum libero. Vestibulum volutpat consequat mi, quis malesuada velit vulputate ut. Curabitur ultricies urna lorem, nec laoreet nulla semper in. Aliquam non faucibus metus. Vestibulum luctus lectus massa, quis pharetra velit placerat vel. Praesent dictum elit eget massa tincidunt, id tincidunt nulla lacinia. Donec velit metus, iaculis ac leo non, egestas volutpat tellus. Cras hendrerit dolor a ornare</p>
      </div>
      <div class="price-box"></div>
    </section>

    <section class="spine">
      <div class="spine-title">CLIMB AND GLOW</div>
      <div class="spine-author">LIONEL BARSTOW</div>
    </section>

    <section class="front-cover">
      <svg class="cover-photo" viewBox="0 0 405 555" role="img" aria-label="Photo of a smiling female speaker holding a microphone and pointing upward">
        <defs>
          <linearGradient id="photoTone" x1="0" y1="0" x2="0" y2="1">
            <stop offset="0" stop-color="var(--photo-mid)"/>
            <stop offset="1" stop-color="var(--photo-light)"/>
          </linearGradient>
        </defs>
        <path d="M274 141 H405 V555 H110 V309 H274 Z" fill="url(#photoTone)"/>
      </svg>
      <h1 class="front-title">
        <span class="line-one">CLIMB AND</span>
        <span class="line-two">GLOW</span>
      </h1>
      <div class="front-rule upper"></div>
      <p class="subtitle">Find Your Voice.<br>Tell Your Story.<br>Share your Message.</p>
      <div class="front-rule lower"></div>
      <div class="author-band">LIONEL BARSTOW</div>
    </section>
  </main>
</body>
</html>
```